Flyer-Design - Coaching & Supervision für freib. Dipl.-Psychologin - BITTE KEINE WEITEREN DESINGS
Zielgruppe
--------- An alle, die überlegen mitzumachen - ich habe gerade als ungefähren Zeitplan, dass ich mich bis Donnerstag Abend (27.01.) entscheide, damit dann am Freitag (+evtl. Wochenende) noch Zeit für das Feintuning ist. -------------------
Ich bin Diplom-Psychologin und arbeite unter anderem freiberuflich als Coach und Supervisorin. Für diese Arbeit brauche ich einen Flyer. Ich habe bereits ein Konzept mit den Inhalten erstellt und brauche dafür nun ein professionelles Layout.
Aufgabenstellung
Anbei finden Sie das Konzept 1x als ppt (inklusive ausprobierter Alternativen zu den Fotos) und 1x als pdf.
Der Flyer hat als zentrales Thema „sich verändern / sich auf den Weg machen“ sowie die Analogie, dass ein gutes Coachinggespräch wie eine Bergtour ist.
Ich habe viel Vorarbeit gemacht (Inhalte stehen, Fotos sind recherchiert…) – sehr gerne können Sie sich kreativ ausleben und was völlig Neues / alles anders machen, es wäre aber auch ok, wenn das bereits Erarbeitete einfach graphisch aufgepimpt und professionalisiert wird.
Mein Wunsch: Ich weiß, dass der Flyer sehr voll ist. Aber ich möchte bewusst relativ viel Info dort unterbringen. Deshalb wäre es gut, wenn die Grafik des Flyers eine gewisse Leichtigkeit beinhaltet, die den vielen Text eher kaschiert. Also nicht zu verschnörkelt, sondern eher schlicht, hell und das Auge entlastend. Ich wünsche mir warme Farbtöne, die einladen und nicht zu kühl-modern wirken.
Logo:
Das Logo habe ich hier auf der Seite gestaltmarkt.de entwickeln lassen und habe alle Rechte daran. Es kann bei Bedarf auch angepasst werden.
Aktuell ist das Logo in grün, da ich dadurch den Naturbezug meiner Metapher mit aufgreife und weil die gerade entstehende Homepage, aktuell auch grün als Grundfarbe hat. Allerdings werde ich die Homepage auch noch professional überarbeiten lassen. Anbei einen Screenshot wie die Startseite der Homepage im Moment so ca. aussieht.
Bilder:
Die Fotos von mir hat ein Fotograf gemacht und ich darf sie verwenden.
Die Landschaftsbilder habe ich kostenlos und lizenzfrei von Lumora Bild ( https://bild.lumora-fotos.de/de/frei ) und von Fotelix ( https://fotelix-bilder.de/de/ ) heruntergeladen.
Falls Sie andere Bilder besser fänden und diese vorschlagen wollen, dann finden Sie weitere Details zu meinen Wünschen an die Bilder im Dokument „SelmK_AusschreibungDetails“
Die Landkarte ist ein Screenshot von KartoWeltNetz. Dort steht i..

```html
<!DOCTYPE html>
<html lang="de">
<head>
<meta charset="utf-8">
<title>Selma Kranich – Coaching &amp; Supervision</title>
<link href="https://fonts.googleapis.com/css2?family=Alegreya:ital,wght@0,500;0,600;1,500&family=Source+Sans+3:wght@400;600&display=swap" rel="stylesheet">
<style>
:root{
  --green:#4e8a2c;
  --green-soft:#7fa35c;
  --panel-green:#e2e5d4;
  --panel-cream:#f3f1ea;
  --orange:#efb24c;
  --ink:#2f2f2f;
  --dark-green:#1f3a1c;
  --white:#ffffff;
}
*{margin:0;padding:0;box-sizing:border-box}
html,body{width:1200px;height:568px;overflow:hidden;background:var(--white)}
body{font-family:"Source Sans 3",sans-serif;color:var(--ink);position:relative}
.abs{position:absolute}
.serif{font-family:"Alegreya",serif}

/* left column */
.qual-panel{left:74px;top:99px;width:293px;height:283px;background:var(--panel-green)}
.about-tab{left:0;top:27px;width:74px;height:135px;background:var(--orange);display:flex;align-items:center;justify-content:center}
.about-tab span{writing-mode:vertical-rl;transform:rotate(180deg);color:var(--white);line-height:1.05}
.about-tab .t1{font-size:19px}
.about-tab .t2{font-size:14px;font-weight:600}
.portrait{left:74px;top:27px;width:200px;height:135px;background:linear-gradient(135deg,#8a7d70,#4a3a30 55%,#b9a894)}
.quals{left:103px;top:183px;width:260px}
.qual{margin-bottom:11px}
.qual h3{font-size:12px;font-weight:600;color:var(--green);line-height:1.15}
.qual p{font-size:9.6px;line-height:1.3}
.experience{left:103px;top:395px;width:260px}
.experience h3{font-size:11.5px;font-weight:400;color:var(--green-soft);line-height:1.15}
.experience ul{list-style:none;margin:6px 0 4px;font-size:9.6px;line-height:1.3}
.experience ul li::before{content:"• "}
.experience small{font-size:9px;color:var(--ink)}

/* middle column */
.location-panel{left:421px;top:27px;width:349px;height:513px;background:var(--panel-cream)}
.location-title{left:421px;top:36px;width:349px;text-align:center}
.location-title h2{font-family:"Alegreya",serif;font-weight:500;font-size:19px;color:var(--green)}
.location-title p{font-size:11px;margin-top:3px}
.map{left:435px;top:92px;width:322px;height:270px;background:linear-gradient(140deg,#d6dfc8,#e8e4da 50%,#cfd9c0)}
.mode{left:394px;height:24px;background:var(--orange);color:var(--white);font-weight:600;font-size:11.5px;display:flex;align-items:center;padding-left:43px}
.walk-text{left:465px;top:385px;width:262px;text-align:center;font-size:9.6px;line-height:1.35}
.contact{left:421px;top:450px;width:349px;text-align:center;color:var(--dark-green)}
.contact h3{font-family:"Alegreya",serif;font-weight:600;font-size:14px;margin-bottom:5px}
.contact p{font-size:11px;line-height:1.25}
.contact .gap{margin-top:4px}

/* right column */
.brand{left:999px;top:40px;display:flex;align-items:center;gap:6px}
.brand-mark{width:30px;height:30px;border-radius:50%;border:2px solid var(--green)}
.brand-name{font-size:15px;color:var(--green);line-height:1}
.cover-title{left:838px;top:110px}
.cover-title h1{font-family:"Alegreya",serif;font-weight:500;font-size:26px;color:var(--green)}
.cover-title p{font-size:12px;margin-top:1px}
.cover-photo{left:824px;top:180px;width:349px;height:360px;background:linear-gradient(150deg,#7fa34e,#5f8a35)}
.questions{left:824px;top:446px;width:251px;height:64px;background:rgba(112,150,88,.92);color:var(--dark-green);font-size:10px;line-height:1.35;padding:5px 0 0 27px}
.promise{left:1022px;top:485px;width:151px;height:42px;background:var(--orange);color:var(--white);font-family:"Alegreya",serif;font-style:italic;font-size:13px;line-height:1.25;padding:4px 0 0 8px}
</style>
</head>
<body>

<div class="abs qual-panel"></div>
<div class="abs about-tab"><span class="t1">Über mich</span><span class="t2">Selma Kranich</span></div>
<div class="abs portrait" role="img" aria-label="Porträtfoto der Psychologin vor hellen Treppenstufen"></div>

<div class="abs quals">
  <div class="qual"><h3>Diplom-Psychologin</h3><p>Schwerpunkte: Arbeits- und Organisationspsychologie;<br>Systemische Familienpsychologie</p></div>
  <div class="qual"><h3>Zertifizierte Coachingausbildung</h3><p>bei TERA München-Berlin e.V. – anerkannt von<br>EVSC (European Venue for Supervision and Coaching)</p></div>
  <div class="qual"><h3>Staatlich zertifizierte<br>Entspannungspädagogin</h3></div>
  <div class="qual"><h3>Kursleiterausbildung</h3><p>(„Train the trainer“) zur Durchführung<br>von Gruppenleiterausbildungen</p></div>
</div>

<div class="abs experience">
  <h3>Berufserfahrung in der Wirtschaft,<br>im sozialen und im kirchlichen Bereich</h3>
  <ul>
    <li>internationaler Großkonzern</li>
    <li>Unternehmensberatung</li>
    <li>Entwicklungshilfe</li>
    <li>Betriebliche Sozialberatung (EAP)</li>
    <li>Berufliche Fortbildungszentren</li>
    <li>Krisenintervention</li>
  </ul>
  <h3>Internationale Erfahrung <small>(Englisches Coaching)</small></h3>
  <ul style="margin-top:2px"><li>1,5 Jahre Philippinen + 1,5 Jahre USA</li></ul>
</div>

<div class="abs location-panel"></div>
<div class="abs location-title">
  <h2>Coaching vor Ort oder Online</h2>
  <p>im Herzen Münchens am Lindenplatz</p>
</div>
<div class="abs map" role="img" aria-label="Stadtkarte von München und Umgebung"></div>
<div class="abs mode" style="top:289px;width:176px">digital oder telefonisch</div>
<div class="abs mode" style="top:319px;width:235px">direkt in Ihrem beruflichen Umfeld</div>
<div class="abs mode" style="top:349px;width:213px">In der Natur und in Bewegung</div>
<p class="abs walk-text">Vielen Menschen fällt es leichter zu reden, wenn sie sich bewegen. Gerne führe ich Gespräche gemeinsam unterwegs in einem Park oder in der freien Natur. Wenn wir uns bewegen, bewegt sich auch etwas in uns.</p>
<div class="abs contact">
  <h3>Kontakt</h3>
  <p>Selma Kranich<br>+49 (0)160 5550 12 34</p>
  <p class="gap">coaching@selmakranich.de<br>www.selmakranich.de</p>
</div>

<div class="abs brand"><span class="brand-mark"></span><span class="brand-name serif">Selma Kranich</span></div>
<div class="abs cover-title">
  <h1>Coaching &amp; Supervision</h1>
  <p>Selma Kranich | Diplom Psychologin</p>
</div>
<div class="abs cover-photo" role="img" aria-label="Foto: Wanderweg über grüne Berghänge unter blauem Himmel"></div>
<div class="abs questions">Stehen Sie vor einer schwierigen Situation?<br>Wollen Sie etwas in Ihrem Leben verändern?<br>Sind Sie irgendwie unzufrieden?<br>Möchten Sie neue Wege gehen?</div>
<div class="abs promise">Ich mache mich mit<br>Ihnen auf den Weg!</div>

</body>
</html>
```